Criminal Defense Law Firm needs Stationary design Theme for a Business Card, Envelope, and Letterhea

Our Law Firm is seeking a general design concept for a business card, letterhead, and Envelope.

Our website is WillowcrestTrialDesk.com

A design for these three items is requested to keep branding in place for the firm. Would like to keep the Firm Colors on the website consistent with our branding on business cards, letterheads, and mailing envelopes #10 size to be exact.

We would like business cards printed front and back with Law firm Colors from website.

Letterhead with law firm colors as well. Design is not limited to just the header, but the footer can be utilized as well for email, website, phone, fax, etc.

Simple #10 envelope consisting of the same design principles set out in the previous two designs.

```html
<!DOCTYPE html>
<html lang="en">
<head>
<meta charset="utf-8">
<title>Willowcrest Trial Law Offices — Business Card</title>
<link rel="stylesheet" href="https://fonts.googleapis.com/css2?family=Alegreya:wght@500&family=Lato:wght@300;400;700&display=swap">
<style>
  :root {
    --gold: #a08f68;
    --teal: #00a3b1;
    --charcoal: #262626;
    --white: #ffffff;
    --paper: #ffffff;
  }
  * { box-sizing: border-box; }
  html, body {
    margin: 0;
    width: 1027px;
    height: 1200px;
    overflow: hidden;
    background: var(--paper);
    font-family: "Lato", sans-serif;
  }
  .canvas { position: relative; width: 1027px; height: 1200px; }

  /* Front side */
  .card-front {
    position: absolute; left: 48px; top: 54px;
    width: 922px; height: 517px;
    background: var(--gold);
    overflow: hidden;
  }
  .front-mark {
    position: absolute; left: 116px; top: 193px;
    width: 114px; height: 114px;
    border: 3px solid var(--white); border-radius: 50%;
  }
  .firm-name {
    position: absolute; left: 269px; top: 205px;
    margin: 0;
    font-family: "Alegreya", serif; font-weight: 500;
    font-size: 40px; line-height: 50px; letter-spacing: 1.5px;
    text-transform: uppercase; color: var(--white);
    white-space: nowrap;
  }
  .web-band {
    position: absolute; left: 0; bottom: 0;
    width: 100%; height: 78px;
    background: var(--teal);
    display: flex; align-items: center; justify-content: center;
  }
  .web-address {
    font-weight: 300; font-size: 40px; color: var(--white);
    letter-spacing: 0.3px; white-space: nowrap;
  }

  /* Back side */
  .card-back {
    position: absolute; left: 48px; top: 628px;
    width: 922px; height: 517px;
    background: var(--charcoal);
  }
  .brand-panel {
    position: absolute; left: 0; top: 0;
    width: 394px; height: 100%;
    background: var(--teal);
  }
  .brand-ring {
    position: absolute; left: 61px; top: 120px;
    width: 275px; height: 275px;
    border: 8px solid var(--white); border-radius: 50%;
    display: flex; align-items: center; justify-content: center;
  }
  .brand-name {
    font-weight: 300; font-size: 38px; color: var(--white);
    white-space: nowrap;
  }
  .person { position: absolute; left: 478px; top: 80px; }
  .person-name {
    margin: 0; font-weight: 300; font-size: 66px; line-height: 68px;
    color: var(--white); text-transform: uppercase; letter-spacing: 1px;
    white-space: nowrap;
  }
  .person-role {
    margin: 0; font-weight: 700; font-size: 26px; line-height: 30px;
    color: var(--gold); letter-spacing: 1px; text-transform: uppercase;
  }
  .contacts {
    position: absolute; left: 477px; top: 199px;
    margin: 0; padding: 0; list-style: none;
  }
  .contact {
    display: flex; align-items: center;
    height: 60px;
    font-weight: 300; font-size: 23px; color: var(--white);
    white-space: nowrap;
  }
  .contact-icon {
    width: 30px; height: 30px; margin-right: 15px; flex: none;
  }
</style>
</head>
<body>
<main class="canvas">

  <section class="card-front" aria-label="Business card front">
    <span class="front-mark" aria-hidden="true"></span>
    <h1 class="firm-name">Willowcrest Trial<br>Law Offices</h1>
    <div class="web-band">
      <span class="web-address">www.willowcresttrialdesk.com</span>
    </div>
  </section>

  <section class="card-back" aria-label="Business card back">
    <div class="brand-panel">
      <div class="brand-ring"><span class="brand-name">Willowcrest</span></div>
    </div>

    <div class="person">
      <h2 class="person-name">Owen Hale</h2>
      <p class="person-role">Lawyer</p>
    </div>

    <ul class="contacts">
      <li class="contact">
        <svg class="contact-icon" viewBox="0 0 32 32" aria-hidden="true">
          <circle cx="16" cy="16" r="16" fill="var(--gold)"/>
          <rect x="11" y="7" width="10" height="18" rx="1.5" fill="none" stroke="#262626" stroke-width="2"/>
          <rect x="13" y="10" width="6" height="9" fill="#262626"/>
        </svg>
        M 555012 48217
      </li>
      <li class="contact">
        <svg class="contact-icon" viewBox="0 0 32 32" aria-hidden="true">
          <circle cx="16" cy="16" r="16" fill="var(--gold)"/>
          <rect x="8" y="10" width="16" height="12" fill="#262626"/>
          <path d="M8 10 L16 17 L24 10" fill="none" stroke="var(--gold)" stroke-width="1.5"/>
        </svg>
        desk@mail.test
      </li>
      <li class="contact">
        <svg class="contact-icon" viewBox="0 0 32 32" aria-hidden="true">
          <circle cx="16" cy="16" r="16" fill="var(--gold)"/>
          <circle cx="16" cy="16" r="8" fill="#262626"/>
        </svg>
        Owen.Hale
      </li>
      <li class="contact">
        <svg class="contact-icon" viewBox="0 0 32 32" aria-hidden="true">
          <circle cx="16" cy="16" r="16" fill="var(--gold)"/>
          <path d="M11 8 L14 8 L15 12 L13 14 C14 17 15 18 18 19 L20 17 L24 18 L24 21 C24 23 22 24 20 24 C14 23 9 18 8 12 C8 10 9 8 11 8 Z" fill="#262626"/>
        </svg>
        + 5550 1742 306
      </li>
    </ul>
  </section>

</main>
</body>
</html>
```